Board to put on a meditation centre - Lantern Grove

I need a board design for a new meditation centre based in Oslo which offers free courses in meditation and self-empowerment. The size of the board is width 374cm x height 104cm.  The name of the meditation centre together with subtitles should be on the board but also some elegant decoration that matches the theme (lantern grove/meditation).
Here is the website of the meditation centre to give you a feeling of it: https://lyktelundsenteret.no/
Good if you can use a blue color close to this one: rgb(37, 180, 193) as well as some brown/golden color (similar to the palette on the website).
On the board it should say:
Lyktelunden (in big letters, the rest is subtitles)
Meditasjon & Spirituell visdom
Kurs - Retreat - Dialog
lyktelundsenteret.no
The design should be very elegant and beautiful and the feeling should be of "An Lantern Grove". A logo is here attached and should be used but I need to get a better quality version of it, will upload that as soon as possible.

```html
<!DOCTYPE html>
<html lang="no">
<head>
<meta charset="UTF-8">
<title>Lyktelunden – skilt</title>
<link rel="stylesheet" href="https://fonts.googleapis.com/css2?family=Archivo:wdth,wght@62..125,400..900&display=swap">
<style>
  :root {
    --backdrop: #3a3939;
    --teal-top: #0f9ea5;
    --teal-deep: #087277;
    --teal-mid: #18a4ab;
    --teal-low: #0e8d93;
    --band-light: #6dc9d2;
    --ink-white: #ffffff;
    --ink-dark: #161616;
    --ornament-core: rgba(255,255,255,0.55);
    --ornament-edge: rgba(255,255,255,0);
  }
  * { margin: 0; padding: 0; box-sizing: border-box; }
  html, body {
    width: 1200px;
    height: 1000px;
    overflow: hidden;
    background: var(--backdrop);
  }
  .canvas {
    position: relative;
    width: 1200px;
    height: 1000px;
  }
  .board {
    position: absolute;
    left: 102px;
    top: 362px;
    width: 995px;
    height: 276px;
    overflow: hidden;
    font-family: "Archivo", "Arial", sans-serif;
    background: linear-gradient(180deg, var(--teal-mid) 0%, var(--teal-low) 100%);
  }
  .board__header {
    position: absolute;
    left: 0; top: 0;
    width: 100%;
    height: 124px;
    background: linear-gradient(180deg, var(--teal-top) 0%, var(--teal-deep) 100%);
    display: flex;
    align-items: center;
    justify-content: center;
  }
  .board__name {
    color: var(--ink-white);
    font-size: 96px;
    font-weight: 800;
    font-stretch: 118%;
    letter-spacing: 2px;
    line-height: 1;
    padding-top: 4px;
  }
  .ornament {
    position: absolute;
    top: 124px;
    width: 150px;
    height: 152px;
    background: radial-gradient(circle at 50% 52%, var(--ornament-core) 0%, rgba(255,255,255,0.3) 35%, var(--ornament-edge) 70%);
  }
  .ornament--left { left: 4px; }
  .ornament--right { right: 4px; }
  .board__tagline {
    position: absolute;
    left: 0; width: 100%;
    top: 137px;
    text-align: center;
    color: var(--ink-white);
    font-size: 28px;
    font-weight: 800;
    font-stretch: 108%;
    letter-spacing: 0.5px;
    padding-left: 8px;
  }
  .board__services {
    position: absolute;
    left: 165px;
    top: 176px;
    width: 652px;
    height: 50px;
    background: var(--band-light);
    display: flex;
    align-items: center;
    justify-content: center;
    color: var(--ink-dark);
    font-size: 34px;
    font-weight: 800;
    font-stretch: 100%;
    letter-spacing: 0.5px;
  }
  .board__web {
    position: absolute;
    left: 0; width: 100%;
    top: 232px;
    text-align: center;
    color: var(--ink-white);
    font-size: 27px;
    font-weight: 400;
    letter-spacing: 0.5px;
    padding-left: 8px;
  }
  .board__web strong { font-weight: 700; }
</style>
</head>
<body>
  <main class="canvas">
    <section class="board" aria-label="Skilt for Lyktelunden">
      <header class="board__header">
        <h1 class="board__name">LYKTELUNDEN</h1>
      </header>
      <div class="ornament ornament--left" role="img" aria-label="Dekorativt strålemotiv i hvitt"></div>
      <div class="ornament ornament--right" role="img" aria-label="Dekorativt strålemotiv i hvitt"></div>
      <p class="board__tagline">MEDITASJON &amp; SPIRITUELL VISDOM</p>
      <p class="board__services">Kurs - Retreat - Dialog</p>
      <p class="board__web">www.<strong>lyktelundsenteret</strong>.no</p>
    </section>
  </main>
</body>
</html>
```